Flyer for Wireless Internet Provider

I'm looking for a new flyer design that is customizable, to target different geographical areas. Not settled on size. Thinking A4/Letter size or A5/half Letter size.
Company website: www.velotrand.dk
I would like to include:Logo / Company name, Contact information, 3 price examples, Coverage map

Target Market(s)

Both private and commercial

Industry/Entity Type

Wireless Internet

```html
<!DOCTYPE html>
<html lang="da">
<head>
<meta charset="utf-8">
<title>Velotrand – Bredbånd flyer</title>
<link rel="stylesheet" href="https://fonts.googleapis.com/css2?family=Open+Sans:wght@400;600;700;800&display=swap">
<style>
  :root {
    --navy: #1b3f78;
    --blue: #1f6fc2;
    --blue-bright: #2a86d8;
    --blue-deep: #123a78;
    --sky: #e9eef4;
    --paper: #ffffff;
    --card-line: #d5d9de;
    --text-dark: #3c4650;
    --yellow: #f6b81b;
    --green: #6cb63c;
    --stage: #e4e6e8;
  }
  * { box-sizing: border-box; margin: 0; padding: 0; }
  html, body { width: 1200px; height: 800px; overflow: hidden; }
  body {
    background: var(--stage);
    font-family: "Open Sans", Arial, sans-serif;
    color: var(--text-dark);
    position: relative;
  }
  .flyer {
    position: absolute; left: 317px; top: 0;
    width: 566px; height: 800px;
    background: var(--sky);
    overflow: hidden;
  }
  /* Header */
  .header { position: absolute; left: 0; top: 0; width: 100%; height: 90px; background: var(--paper); }
  .brand {
    position: absolute; left: 36px; top: 26px;
    display: flex; align-items: center; gap: 8px;
    font-weight: 800; font-size: 22px; color: var(--navy);
  }
  .brand-dot { width: 14px; height: 14px; border-radius: 50%; background: var(--navy); }
  .header-band { position: absolute; right: 0; top: 10px; width: 300px; height: 70px; }
  .header-url {
    position: absolute; right: 80px; top: 28px;
    color: #fff; font-weight: 700; font-size: 13px; letter-spacing: .3px;
  }
  /* Hero */
  .hero {
    position: absolute; left: 0; top: 90px; width: 100%; height: 300px;
    background: linear-gradient(180deg, #3f5b86 0%, #5a7396 40%, #7f8fa4 70%, #b9c1cb 100%);
  }
  .hero-shade {
    position: absolute; left: 0; top: 90px; width: 100%; height: 300px;
    background: linear-gradient(90deg, rgba(22,52,104,.75) 0%, rgba(22,52,104,.25) 60%, rgba(22,52,104,0) 100%);
  }
  .hero-tag {
    position: absolute; left: 0; top: 100px; width: 210px; height: 56px;
    background: rgba(40,90,160,.75);
  }
  .hero-title { position: absolute; left: 36px; top: 113px; color: #fff; font-weight: 800; font-size: 24px; letter-spacing: .5px; }
  .hero-sub { position: absolute; left: 36px; top: 162px; color: #fff; font-weight: 800; font-size: 22px; line-height: 1.15; }
  .hero-lead { position: absolute; left: 36px; top: 260px; color: #fff; font-weight: 700; font-size: 17px; line-height: 1.3; letter-spacing: .3px; }
  .contact-chip {
    position: absolute; right: 0; top: 280px; width: 190px; height: 56px;
    background: var(--blue);
    clip-path: polygon(10% 0, 100% 0, 100% 100%, 0 100%);
    display: flex; align-items: center; gap: 12px; padding-left: 40px;
    color: #fff; font-weight: 700; font-size: 12px; line-height: 1.35;
  }
  /* Pricing */
  .plans { position: absolute; left: 32px; top: 365px; width: 502px; display: flex; gap: 20px; }
  .plan { flex: 1; background: var(--paper); box-shadow: 0 2px 6px rgba(0,0,0,.15); padding-bottom: 10px; }
  .plan-speed { height: 38px; display: flex; align-items: center; justify-content: center; font-weight: 600; font-size: 15px; color: #4a5560; background: #f3f4f5; }
  .plan-price { height: 38px; display: flex; align-items: center; justify-content: center; font-weight: 800; font-size: 16px; color: #fff; }
  .plan-price.yellow { background: var(--yellow); }
  .plan-price.blue { background: var(--blue); }
  .plan-price.green { background: var(--green); }
  .plan-features { list-style: none; padding: 6px 10px 0; }
  .plan-features li { font-size: 10px; text-align: center; padding: 6px 0; border-bottom: 1px solid var(--card-line); line-height: 1.3; }
  .plan-features li:last-child { border-bottom: none; }
  /* Footer */
  .footer {
    position: absolute; left: 0; top: 575px; width: 100%; height: 225px;
    background: linear-gradient(135deg, var(--blue-bright) 0%, var(--blue) 45%, var(--blue-deep) 100%);
    color: #fff;
  }
  .footer-divider { position: absolute; left: 242px; top: 22px; width: 1px; height: 150px; background: rgba(255,255,255,.35); }
  .footer h2 { font-size: 17px; font-weight: 800; letter-spacing: .5px; }
  .contact-block { position: absolute; left: 44px; top: 18px; width: 190px; }
  .contact-intro { font-size: 10.5px; font-weight: 700; line-height: 1.35; margin: 4px 0 10px; }
  .contact-list { list-style: none; }
  .contact-list li { display: flex; gap: 10px; align-items: flex-start; font-size: 10px; line-height: 1.35; margin-bottom: 9px; }
  .contact-list svg { flex: none; width: 14px; height: 14px; }
  .solutions { position: absolute; left: 290px; top: 18px; }
  .solutions ul { list-style: none; margin-top: 6px; }
  .solutions li { font-size: 11px; font-weight: 700; margin-bottom: 5px; display: flex; align-items: center; gap: 8px; }
  .solutions li::before { content: ""; width: 5px; height: 5px; border-radius: 50%; background: #fff; }
  .footer-foot { position: absolute; left: 0; bottom: 0; width: 100%; height: 24px; }
</style>
</head>
<body>
<main class="flyer">
  <header class="header">
    <div class="brand"><span class="brand-dot"></span>Velotrand.dk</div>
    <svg class="header-band" viewBox="0 0 300 70" aria-hidden="true">
      <polygon points="60,10 300,10 300,60 40,60" fill="#1f6fc2"/>
      <polygon points="20,28 120,28 108,50 8,50" fill="#123a78"/>
      <polygon points="230,0 300,0 300,22 220,22" fill="#2a86d8"/>
    </svg>
    <div class="header-url">www.velotrand.dk</div>
  </header>

  <section>
    <div class="hero" role="img" aria-label="Foto af et boligkvarter med huse og trådløst signal i skumringen"></div>
    <div class="hero-shade"></div>
    <div class="hero-tag"></div>
    <h1 class="hero-title">BREDBÅND</h1>
    <p class="hero-sub">Træt af langsomt<br>internet??</p>
    <p class="hero-lead">Velotrand leverer hurtige<br>internet forbindelser trådløst.</p>
    <div class="contact-chip">
      <svg width="22" height="20" viewBox="0 0 22 20" aria-hidden="true">
        <path d="M2 2h18v12H9l-5 4v-4H2z" fill="none" stroke="#fff" stroke-width="1.8" stroke-linejoin="round"/>
        <circle cx="7" cy="8" r="1.3" fill="#fff"/><circle cx="11" cy="8" r="1.3" fill="#fff"/><circle cx="15" cy="8" r="1.3" fill="#fff"/>
      </svg>
      <span>KONTAKT<br>31 84 62 05</span>
    </div>
  </section>

  <section class="plans">
    <article class="plan">
      <div class="plan-speed">20/20 Mbit</div>
      <div class="plan-price yellow">199 kr./md</div>
      <ul class="plan-features">
        <li>Ubegrænset forbrug</li><li>Ingen binding</li><li>Diskret udendørs antenne</li><li>Tilbud på installation,<br>kun 500 kr.</li>
      </ul>
    </article>
    <article class="plan">
      <div class="plan-speed">50/50 Mbit</div>
      <div class="plan-price blue">299 kr./md</div>
      <ul class="plan-features">
        <li>Ubegrænset forbrug</li><li>Ingen binding</li><li>Diskret udendørs antenne</li><li>Tilbud på installation,<br>kun 500 kr.</li>
      </ul>
    </article>
    <article class="plan">
      <div class="plan-speed">100/100 Mbit</div>
      <div class="plan-price green">399 kr./md</div>
      <ul class="plan-features">
        <li>Ubegrænset forbrug</li><li>Ingen binding</li><li>Diskret udendørs antenne</li><li>Tilbud på installation,<br>kun 500 kr.</li>
      </ul>
    </article>
  </section>

  <footer class="footer">
    <div class="contact-block">
      <h2>KONTAKT</h2>
      <p class="contact-intro">Har du spørgsmål, ris eller ros,<br>kontakt Velotrand.</p>
      <ul class="contact-list">
        <li><svg viewBox="0 0 14 14" aria-hidden="true"><path d="M3 1l2 3-1.3 1.5a7 7 0 0 0 4.8 4.8L10 9l3 2-1.5 2.5C6 13 1 8 0.8 2.5z" fill="#fff"/></svg>31 84 62 05</li>
        <li><svg viewBox="0 0 14 14" aria-hidden="true"><rect x="1" y="3" width="12" height="8" fill="none" stroke="#fff" stroke-width="1.3"/><path d="M1 3l6 5 6-5" fill="none" stroke="#fff" stroke-width="1.3"/></svg>mail@velotrand.dk</li>
        <li><svg viewBox="0 0 14 14" aria-hidden="true"><rect x="1" y="2" width="12" height="10" rx="1" fill="none" stroke="#fff" stroke-width="1.3"/><line x1="1" y1="5" x2="13" y2="5" stroke="#fff" stroke-width="1.3"/></svg>www.velotrand.dk</li>
        <li><svg viewBox="0 0 14 14" aria-hidden="true"><rect x="2" y="2" width="10" height="11" fill="none" stroke="#fff" stroke-width="1.3"/><path d="M5 5h1M8 5h1M5 8h1M8 8h1" stroke="#fff" stroke-width="1.3"/></svg>Velotrand er en del af Nord Data<br>Kildebakken 12, 4600 Ørsby</li>
      </ul>
    </div>
    <div class="footer-divider"></div>
    <div class="solutions">
      <h2>LØSNINGER</h2>
      <ul>
        <li>Bredbånd / Internet forbindelse</li>
        <li>Dedikeret internet forbindelse</li>
        <li>Offentlig IP adresse</li>
        <li>LAN to LAN</li>
        <li>Hosted firewall</li>
        <li>Hosted VPN</li>
        <li>Hosted video overvågning</li>
        <li>Hosting af fysiske eller virtuelle servere</li>
      </ul>
    </div>
    <svg class="footer-foot" viewBox="0 0 566 24" preserveAspectRatio="none" aria-hidden="true">
      <polygon points="0,24 0,10 160,10 175,24" fill="#e9eef4"/>
      <polygon points="380,24 395,12 566,12 566,24" fill="#0f3268"/>
    </svg>
  </footer>
</main>
</body>
</html>
```